NURSING: RISING PAST THE SHADOWED SILL

Size of the book cover: 140 x 215 mms

I need a cover for the 30,000 word book I have just written. It is a positive take on what I think nursing is and what it needs to be in the future. It is also my story of being nursed and of being a nurse.

My dream is that nurses honor themselves; that they look to the future with confidence and intelligence and that care continues to be delivered with compassionate person centeredness.

I define nursing as a professional workforce which, with probity, prevent or relieve distress; provide compassionate, safe, excellent care; and which contributes to the organization of healthcare.

The name comes from a Biblical parable Corlan 3:7-9. If a light is hidden under a bushel (basket) it is barely seen. If it is lit out from the basket it is clearly seen. As nurses we must continue to take up our mantel and ensure our light is seen and that it continues to shine the way we want it to.

As nurses we each take up our own lantern of caring, each in our own ways. To walk more brightly in our own paths of service.

The final design should show the specialness of nursing.

Target Market(s)

Nurses present, past and future

Industry/Entity Type

Healthcare

Font styles to use
Sans Serif
Other font styles liked:
• Whatever you think will suit

Colors
ec1f27
0393ce
9bcb3c

Requirements
Must have
• Be friendly, calming.
• NB: I am not sure whether the title should be in uppercase or not. Nursing could be uppercase and rising past the shadowed sill could be lower case. I leave it to you experienced people
Nice to have
• Something that depicts nursing...or is suggestive of nursing and the specialness of the work we do. How we bring our light to our patients as we 'hold them in the palms of out hands' and care for them. How they honor us by allowing us into their lives. Our rich past and out history allows us to be who we are today and we look to the future with confidence and hope
• I like rich colors, eg the color type you might find on a stained glass window in a church - rich emerald green or rich crimson red or the deep blue of a nurses cape
Should not have
• A dark cover
• clutter
• Religious overtone
• I have chosen three colors but they are not in the shading I would like - see above

```html
<!DOCTYPE html>
<html lang="en">
<head>
<meta charset="utf-8">
<title>Nursing: Rising Past the Shadowed Sill — Cover</title>
<link rel="stylesheet" href="https://fonts.googleapis.com/css2?family=Londrina+Solid:wght@400;900&family=Open+Sans:wght@400;600&display=swap">
<style>
  :root {
    --backdrop: #ece9e4;
    --cape-blue: #2389bf;
    --sage-green: #93b851;
    --emerald: #62b52b;
    --crimson: #cf373e;
    --title-fill: #e8eef2;
    --ink: #1f2a33;
    --quote: #f2f6f9;
    --author: #f6dfe0;
  }
  * { margin: 0; padding: 0; box-sizing: border-box; }
  html, body {
    width: 1200px; height: 789px; overflow: hidden;
    background: var(--backdrop);
  }
  .canvas {
    position: relative; width: 1200px; height: 789px;
  }
  .cover {
    position: absolute; left: 359px; top: 24px;
    width: 482px; height: 740px;
    overflow: hidden;
    box-shadow: 0 6px 22px rgba(0,0,0,0.18);
    font-family: "Open Sans", sans-serif;
  }
  .cover-art { position: absolute; inset: 0; width: 100%; height: 100%; display: block; }
  .figure-area {
    position: absolute; left: 8%; top: 4%; width: 48%; height: 96%;
    background: radial-gradient(ellipse at 40% 35%, rgba(60,80,70,0.12), rgba(60,80,70,0) 70%);
  }
  .title {
    position: absolute; right: 22px; top: 92px;
    font-family: "Londrina Solid", sans-serif; font-weight: 900;
    font-size: 96px; line-height: 1; letter-spacing: 6px;
    color: var(--title-fill);
    -webkit-text-stroke: 2px #5a6f80;
  }
  .subtitle {
    position: absolute; right: 22px; top: 198px;
    font-size: 21px; font-weight: 400; letter-spacing: 0.3px;
    color: var(--ink); white-space: nowrap;
  }
  .quote {
    position: absolute; left: 218px; top: 318px; width: 252px;
    font-size: 13.5px; line-height: 1.2; text-align: center;
    color: var(--quote);
  }
  .author {
    position: absolute; left: 300px; bottom: 32px;
    font-size: 17px; color: var(--author);
  }
  .foreword {
    position: absolute; left: 28px; bottom: 26px;
    font-size: 10px; color: var(--ink);
  }
</style>
</head>
<body>
<main class="canvas">
  <section class="cover" aria-label="Book cover">
    <svg class="cover-art" viewBox="0 0 140 215" preserveAspectRatio="none" aria-hidden="true">
      <rect class="field-blue" width="140" height="215" fill="var(--cape-blue)"/>
      <polygon class="field-emerald" points="75,114 140,131 140,215" fill="var(--emerald)"/>
      <polygon class="field-sage" points="0,0 140,215 0,140" fill="var(--sage-green)"/>
      <polygon class="field-crimson" points="0,128 140,210 140,215 0,215" fill="var(--crimson)"/>
    </svg>
    <div class="figure-area" role="img" aria-label="Faint line illustration of a nurse in profile with a cap, overlaid across the cover"></div>
    <h1 class="title">NURSING</h1>
    <p class="subtitle">RISING PAST THE SHADOWED SILL</p>
    <p class="quote">“We each take up our own lantern of caring, each in our own ways, to walk more brightly in our own path of service”</p>
    <p class="author">Mara Ellison</p>
    <p class="foreword">Forward by Ruth Calder RN</p>
  </section>
</main>
</body>
</html>
```